New website for a commercial real estate consulting company

What we’re looking for in a new web site:
• Desktop and mobile friendly
• Clear navigation
• Strong graphics
• Professional appearance
• The ability to update it ourselves
• Site is for information purposes only – no transactions required
• Traffic counts – number of visits per page?
• A firm quote on costs to develop and launch
• SSL
Attached is a copy of the revised text we propose to use, including our new logo. (The pagination can be different than as shown.)
Our current website address is www.brightlanecounselgroup.ca

```html
<!DOCTYPE html>
<html lang="en">
<head>
<meta charset="utf-8">
<title>Contact Us – Brightlane Counsel Group</title>
<link rel="stylesheet" href="https://fonts.googleapis.com/css2?family=Montserrat:wght@400;500;600;700&family=Roboto:wght@400&display=swap">
<style>
  :root {
    --page-bg: #f4f4f4;
    --header-bg: #ffffff;
    --ink: #1c1c1c;
    --muted: #7a7a7a;
    --nav: #8a8a8a;
    --nav-active: #2b3a8f;
    --brand: #2b3a8f;
    --accent: #12cbc4;
    --field: #ffffff;
    --map-a: #d9d9d9;
    --map-b: #c4c4c4;
    --footer: #121212;
  }
  * { box-sizing: border-box; margin: 0; padding: 0; }
  html, body { width: 1200px; height: 1200px; overflow: hidden; }
  body { background: var(--page-bg); font-family: "Montserrat", sans-serif; color: var(--ink); position: relative; }

  .site-header { position: absolute; top: 0; left: 0; width: 1200px; height: 112px; background: var(--header-bg); }
  .brand { position: absolute; left: 86px; top: 42px; display: flex; align-items: center; gap: 8px; }
  .brand-mark { width: 14px; height: 14px; background: var(--brand); }
  .brand-name { font-weight: 600; font-size: 13px; letter-spacing: 1.5px; color: var(--brand); text-transform: uppercase; line-height: 1.3; }
  .main-nav { position: absolute; right: 74px; top: 54px; display: flex; gap: 28px; }
  .main-nav a { font-size: 11px; font-weight: 500; letter-spacing: 1.3px; color: var(--nav); text-decoration: none; text-transform: uppercase; }
  .main-nav a.is-active { color: var(--nav-active); }

  .contact-info { position: absolute; left: 86px; top: 172px; width: 400px; }
  .contact-title { font-size: 27px; font-weight: 700; letter-spacing: 0.3px; }
  .contact-intro { margin-top: 24px; font-size: 14px; line-height: 21px; color: var(--muted); }
  .details { margin-top: 70px; list-style: none; font-size: 14px; }
  .details li { height: 31.6px; }
  .details .label { color: var(--ink); font-weight: 500; margin-right: 6px; }
  .details .value { color: var(--muted); }
  .details .indent { padding-left: 71px; color: var(--muted); }

  .contact-form { position: absolute; left: 524px; top: 176px; width: 589px; font-family: "Roboto", sans-serif; }
  .field { position: absolute; background: var(--field); font-size: 14px; color: var(--muted); padding: 14px 18px; }
  .field-name { left: 0; top: 0; width: 281px; height: 42px; }
  .field-email { left: 308px; top: 0; width: 281px; height: 42px; }
  .field-title { left: 0; top: 68px; width: 589px; height: 42px; }
  .field-comment { left: 0; top: 137px; width: 589px; height: 149px; padding-top: 14px; }
  .send-btn { position: absolute; left: 0; top: 312px; width: 158px; height: 47px; background: var(--accent); color: #fff; border: 0; font-family: "Montserrat", sans-serif; font-size: 12px; font-weight: 500; letter-spacing: 1.3px; text-transform: uppercase; }

  .location-map { position: absolute; left: 85px; top: 625px; width: 1026px; height: 412px; background: linear-gradient(135deg, var(--map-a), var(--map-b) 55%, var(--map-a)); }
  .location-map .pin { position: absolute; left: 561px; top: 149px; }

  .site-footer { position: absolute; left: 0; top: 1124px; width: 1200px; height: 76px; background: var(--footer); }
  .footer-brand { position: absolute; left: 120px; top: 48px; display: flex; align-items: center; gap: 6px; }
  .footer-brand .brand-mark { background: #fff; width: 10px; height: 10px; }
  .footer-brand .brand-name { color: #fff; font-size: 10px; }
</style>
</head>
<body>
  <header class="site-header">
    <div class="brand">
      <span class="brand-mark"></span>
      <span class="brand-name">Brightlane<br>Counsel Group</span>
    </div>
    <nav class="main-nav">
      <a href="#">Home</a>
      <a href="#">Who We Are</a>
      <a href="#">What We Do</a>
      <a href="#" class="is-active">Contact Us</a>
      <a href="#">Industry Events Calendar</a>
    </nav>
  </header>

  <section class="contact-info">
    <h1 class="contact-title">Contact Us</h1>
    <p class="contact-intro">To discuss your real estate needs in confidence,<br>please contact:</p>
    <ul class="details">
      <li><span class="label">Name:</span><span class="value">Maren Holloway</span></li>
      <li><span class="label">Telephone:</span><span class="value">905.555.0142</span></li>
      <li><span class="label">Cell:</span><span class="value">905.555.0187</span></li>
      <li><span class="label">Email:</span><span class="value">maren.holloway@brightlanecounselgroup.ca</span></li>
      <li><span class="label">Address:</span><span class="value">Brightlane Counsel Group, 418 Linden Avenue</span></li>
      <li class="indent">Milbrook, Ontario&nbsp; K0L 2M4</li>
    </ul>
  </section>

  <form class="contact-form">
    <div class="field field-name">Your Name</div>
    <div class="field field-email">Your Email</div>
    <div class="field field-title">Your Title</div>
    <div class="field field-comment">Your Comment</div>
    <button type="button" class="send-btn">Send Message</button>
  </form>

  <div class="location-map" role="img" aria-label="Greyscale street map showing the office location">
    <svg class="pin" width="20" height="28" viewBox="0 0 20 28">
      <path d="M10 0C4.5 0 0 4.4 0 9.8 0 17 10 28 10 28s10-11 10-18.2C20 4.4 15.5 0 10 0z" fill="#000"/>
      <circle cx="10" cy="9.5" r="3.6" fill="#fff"/>
    </svg>
  </div>

  <footer class="site-footer">
    <div class="footer-brand">
      <span class="brand-mark"></span>
      <span class="brand-name">Brightlane</span>
    </div>
  </footer>
</body>
</html>
```